Letterhead for denture company

We need a letterhead designed for our denture company called "Brightmolars" We have attached the logo and business card with the colours on them that we like

Target Market(s)

Everyone aged 45+

Industry/Entity Type

Dental Clinic

Font styles to use
Serif
Sans Serif

Colors
3276b5
f37122

Requirements
Must have
• The colours used in our business card
• Be bold and modern
• Thick fonts
• Logo
Nice to have
• Elements that could tie in nicely with any future signage or website upgrades
Should not have
• Thin font
• Should not be too busy

```html
<!DOCTYPE html>
<html lang="en">
<head>
<meta charset="utf-8">
<title>Brightmolars Letterhead</title>
<link href="https://fonts.googleapis.com/css2?family=Lato:wght@400;700;900&display=swap" rel="stylesheet">
<style>
  :root {
    --blue: #1f6bb8;
    --orange: #e05f26;
    --ink: #1a1a1a;
    --grey: #7a7a7a;
    --paper: #ffffff;
    --backdrop: #ececec;
  }
  * { margin: 0; padding: 0; box-sizing: border-box; }
  html, body { width: 1200px; height: 888px; overflow: hidden; background: var(--backdrop); font-family: 'Lato', sans-serif; }
  .canvas { position: relative; width: 1200px; height: 888px; }
  .sheet { position: absolute; top: 78px; width: 513px; height: 727px; background: var(--paper); overflow: hidden; }
  .sheet--cover { left: 65px; }
  .sheet--letter { left: 629px; }

  .brand { position: absolute; display: flex; flex-direction: column; align-items: center; }
  .brand__mark { background: var(--blue); }
  .brand__name { font-family: 'Lato', sans-serif; font-weight: 900; color: var(--blue); letter-spacing: 0.5px; white-space: nowrap; }

  .sheet--cover .brand { left: 0; right: 0; top: 304px; }
  .sheet--cover .brand__mark { width: 52px; height: 52px; }
  .sheet--cover .brand__name { font-size: 30px; margin-top: 8px; }

  .letter__accent { position: absolute; left: 0; top: 45px; width: 53px; height: 58px; background: var(--orange); }
  .sheet--letter .brand { left: 70px; width: 160px; top: 44px; }
  .sheet--letter .brand__mark { width: 32px; height: 32px; }
  .sheet--letter .brand__name { font-size: 19px; margin-top: 7px; }

  .contact { position: absolute; left: 293px; top: 45px; width: 220px; height: 58px; background: var(--blue); color: #fff; padding: 8px 12px; display: flex; }
  .contact__person { flex: 1; }
  .contact__name { font-weight: 900; font-size: 10px; letter-spacing: 0.3px; }
  .contact__role { font-size: 6.5px; opacity: 0.85; margin-top: 1px; }
  .contact__address { font-size: 6.5px; line-height: 8.5px; margin-top: 7px; opacity: 0.9; }
  .contact__lines { border-left: 1px solid rgba(255,255,255,0.7); padding-left: 10px; margin-top: 18px; height: 25px; font-size: 6.5px; line-height: 8.5px; }
  .contact__lines li { list-style: none; display: flex; align-items: center; gap: 4px; }
  .contact__lines svg { width: 5px; height: 5px; fill: #fff; }

  .letter__body { position: absolute; left: 55px; top: 198px; width: 420px; font-size: 9.6px; line-height: 12.4px; color: var(--ink); }
  .letter__body p { margin-bottom: 12.4px; }
  .letter__body .gap { margin-bottom: 37px; }
  .letter__signature { position: absolute; left: 354px; top: 555px; width: 100px; height: 75px; background: linear-gradient(135deg, #f4f4f4, #e8e8e8); border-radius: 4px; }

  .letter__footer { position: absolute; left: 0; bottom: 0; width: 513px; height: 32px; }
</style>
</head>
<body>
<main class="canvas">
  <section class="sheet sheet--cover">
    <div class="brand">
      <div class="brand__mark"></div>
      <div class="brand__name">BRIGHTMOLARS</div>
    </div>
  </section>

  <section class="sheet sheet--letter">
    <div class="letter__accent"></div>
    <div class="brand">
      <div class="brand__mark"></div>
      <div class="brand__name">BRIGHTMOLARS</div>
    </div>
    <div class="contact">
      <div class="contact__person">
        <div class="contact__name">LIAM HARKER</div>
        <div class="contact__role">Dental prosthetist</div>
        <div class="contact__address">41 Kowhai Street<br>Greenhill, Auckland</div>
      </div>
      <ul class="contact__lines">
        <li><svg viewBox="0 0 10 10"><circle cx="5" cy="5" r="5"/></svg>080055 4120</li>
        <li><svg viewBox="0 0 10 10"><rect width="10" height="8" y="1"/></svg>liam@brightmolars.co.nz</li>
        <li><svg viewBox="0 0 10 10"><circle cx="5" cy="5" r="5"/></svg>www.brightmolars.co.nz</li>
      </ul>
    </div>

    <div class="letter__body">
      <p>2250, Maple Crest Avenue<br>Los Angeles, CA 90012.</p>
      <p>January 29th, 2011</p>
      <p>Mr. Halvorsen<br>President, Halvorsen Family Center<br>518 Orchard Lane<br>New York, NY 10031</p>
      <p>Dear Mr. Halvorsen:</p>
      <p class="gap">In the first paragraph, one needs to give a brief introduction of oneself. One should also give reference to the purpose of the letter in brief.The second paragraph needs to give the details of the letter and its need. This paragraph is mostly longer than the others and plays the main role in the letter. Keep the sentences short and to the point. Avoid using complex words and sentences.</p>
      <p>The third and last paragraph is the conclusion of the letter and can be kept short.</p>
      <p>Sincerely,</p>
      <p>(this is where the signature of the writer will be placed)</p>
      <p>Dana Whitfield<br>More letter guides at: http://www.letterguide-sample.com/articles/business-letter-layout.html</p>
    </div>
    <div class="letter__signature" role="img" aria-label="Handwritten signature of the letter writer"></div>

    <svg class="letter__footer" viewBox="0 0 513 32" preserveAspectRatio="none">
      <path d="M0 13 H298 Q310 13 314 9 L300 22 H0 Z" fill="var(--orange)"/>
      <path d="M0 24 H300 Q308 24 312 18 Q320 2 345 2 H513 V32 H0 Z" fill="var(--blue)"/>
    </svg>
  </section>
</main>
</body>
</html>
```